Zielgruppe
Endkunde ist eine Immobilienfirma ((Bauträger)
Aufgabenstellung
Das Design soll für eine Präsentationsmappe erstellt werden und die Bemaßung sowie Farbigleit der vorgegebnen pdf-Datei beinhalten. Es soll in den Hausfarben , nebst den Backround in grau, gehalten werden.

```html
<!DOCTYPE html>
<html lang="de">
<head>
<meta charset="utf-8">
<title>Wertbau Elbland AG – Präsentationsmappe</title>
<link href="https://fonts.googleapis.com/css2?family=Gelasio&family=Heebo:wght@300;400;700&display=swap" rel="stylesheet">
<style>
  :root {
    --brand-red: #8b1a14;
    --link-red: #b2585a;
    --text-grey: #4a4a4a;
    --die-line: #b3534f;
    --guide-blue: #5ec4ea;
    --paper: #ffffff;
    --photo-light: #e6e6e6;
    --photo-dark: #6f6f6f;
  }
  * { margin: 0; padding: 0; box-sizing: border-box; }
  html, body { width: 1200px; height: 900px; overflow: hidden; background: var(--paper); }
  .folder { position: relative; width: 1200px; height: 900px; font-family: "Heebo", sans-serif; color: var(--text-grey); }
  .dieline { position: absolute; inset: 0; }
  .abs { position: absolute; white-space: nowrap; }
  .right { text-align: right; }

  .brand-name { font-family: "Gelasio", serif; color: var(--brand-red); font-weight: 400; line-height: 1.05; }
  .brand-square { position: absolute; background: var(--brand-red); }

  .flap-brand { right: 1082px; top: 133px; font-size: 13px; }
  .flap-square { left: 92px; top: 108px; width: 22px; height: 22px; }

  .flap-contact { right: 1080px; font-size: 9.2px; line-height: 11.3px; }
  .flap-contact.main { top: 492px; }
  .flap-contact.branch { top: 603px; }
  .flap-contact p + p { margin-top: 11px; }
  .flap-divider { position: absolute; left: 30px; top: 586px; width: 91px; border-top: 1px dotted var(--die-line); }

  .back-brand { right: 876px; top: 334px; font-size: 20px; }
  .back-square { left: 336px; top: 330px; width: 38px; height: 38px; }
  .back-address { right: 822px; top: 426px; font-size: 9px; line-height: 11px; font-weight: 300; }
  .back-address p + p { margin-top: 10px; }
  .back-web { right: 822px; top: 481px; font-size: 20.5px; line-height: 24px; font-weight: 300; color: var(--link-red); }

  .front-brand { left: 729px; top: 160px; font-size: 23px; }
  .front-brand span { display: block; text-align: right; }
  .front-square { left: 740px; top: 100px; width: 50px; height: 50px; }

  .front-photo { position: absolute; left: 729px; top: 341px; width: 280px; height: 389px;
    background: linear-gradient(160deg, var(--photo-light) 0%, #cfcfcf 45%, var(--photo-dark) 100%); }

  .tagline { right: 57px; top: 433px; font-size: 13px; line-height: 15.5px; font-weight: 300; color: #333; }
  .tagline strong { display: block; font-size: 18.5px; line-height: 22px; font-weight: 700; color: var(--brand-red); letter-spacing: 0.3px; }
  .front-web { right: 57px; top: 667px; font-size: 13px; color: var(--brand-red); }
</style>
</head>
<body>
<div class="folder">
  <svg class="dieline" width="1200" height="900" viewBox="0 0 1200 900" aria-hidden="true">
    <g fill="none" stroke="var(--die-line)" stroke-width="0.7" stroke-dasharray="3 2">
      <path d="M138 12 L24 38 Q12 44 12 60 L12 689 Q12 703 24 707 L138 730"/>
      <path d="M138 12 L1188 12 L1188 730 L660 730"/>
      <path d="M149 743 L184 777 L184 789 L175 784 Q160 805 170 830 Q190 862 241 857 L250 853 L245 846 L250 845 L279 872 L613 872 Q635 872 640 850 L660 743"/>
    </g>
    <g stroke="var(--guide-blue)" stroke-width="0.7">
      <line x1="139" y1="12" x2="139" y2="728"/>
      <line x1="149" y1="12" x2="149" y2="728"/>
      <line x1="660" y1="12" x2="660" y2="728"/>
      <line x1="675" y1="12" x2="675" y2="728"/>
      <line x1="149" y1="730" x2="660" y2="730"/>
      <line x1="149" y1="742" x2="660" y2="742"/>
    </g>
    <g fill="var(--brand-red)">
      <rect x="12" y="398" width="366" height="4.5"/>
      <rect x="869" y="398" width="319" height="4.5"/>
    </g>
  </svg>

  <!-- Inside flap -->
  <div class="brand-square flap-square"></div>
  <div class="abs right brand-name flap-brand">Wertbau Elbland AG</div>

  <div class="abs right flap-contact main">
    <p>Lindenhofweg 7,<br>01468 Moritzstein</p>
    <p>Telefon:<br>03 51 – 48 62 10-11<br>Telefax:<br>03 51 – 48 62 10-12</p>
  </div>
  <div class="flap-divider"></div>
  <div class="abs right flap-contact branch">
    <p>Amselgasse 12<br>89547 Talbrunn</p>
    <p>Telefon:<br>+49 7321 550218<br>Telefax:<br>+49 7321 55029</p>
  </div>

  <!-- Back cover -->
  <div class="abs right brand-name back-brand">Wertbau<br>Elbland AG</div>
  <div class="brand-square back-square"></div>
  <div class="abs right back-address">
    <p>Lindenhofweg 7, 01468 Moritzstein</p>
    <p>Telefon: 03 51 – 48 62 10-11<br>Telefax: 03 51 – 48 62 10-12</p>
  </div>
  <div class="abs right back-web">info@wba-ag.de<br>www.wba-ag.de</div>

  <!-- Front cover -->
  <div class="brand-square front-square"></div>
  <div class="abs brand-name front-brand">Wertbau<span>Elbland AG</span></div>

  <div class="front-photo" role="img" aria-label="Schwarzweißfoto moderner mehrgeschossiger Wohngebäude mit Balkonen und begrüntem Vorgarten"></div>

  <div class="abs right tagline">Ihre Zufriedenheit<br>ist unsere<strong>MOTIVATION</strong></div>
  <div class="abs right front-web">www.wba-ag.de</div>
</div>
</body>
</html>
```